International Trading Company, 'KIRO' needs a Business Card

The company name is "KIRO" and it has own logo design.
I'd like to use its logo on this business card.
I need two side Business Card.
I'll look forward to your great design.
Thank you very much in advance.

Contact Information for Business Card

Company Name : Kiro Harbour Limited
Information Example
Dorian Pallister
Mobile(use icon please) : 1 (212) 555-0143
Tel(use icon please) : 1 (212) 555-0178
Email(use icon please) : dorian27@kiroharbour-mail.com
Address(use icon please) : 482 Halden Ave, New York, NY 10160, USA

```html
<!DOCTYPE html>
<html lang="en">
<head>
<meta charset="utf-8">
<title>Kiro Harbour Limited – Business Card</title>
<link href="https://fonts.googleapis.com/css2?family=Lato:wght@400;700&display=swap" rel="stylesheet">
<style>
  :root {
    --page-bg: #e9e6e1;
    --card-dark: #2f2f31;
    --card-dark-mark: #454547;
    --card-light: #ffffff;
    --ink: #4a4a4c;
    --ink-strong: #2a2a2c;
    --ink-soft: #6d6d70;
    --rule: #5a5a5c;
  }
  * { box-sizing: border-box; margin: 0; padding: 0; }
  html, body {
    width: 1200px; height: 800px; overflow: hidden;
    background: var(--page-bg);
    font-family: "Lato", sans-serif;
  }
  .canvas {
    width: 1200px; height: 800px;
    display: flex; align-items: center; justify-content: center; gap: 40px;
  }
  .card {
    position: relative;
    width: 540px; height: 309px;
    border-radius: 18px;
    box-shadow: 0 10px 28px rgba(0,0,0,0.18);
    overflow: hidden;
  }
  /* Front */
  .card--front { background: var(--card-dark); }
  .front-brand {
    position: absolute; left: 0; right: 0; top: 96px;
    text-align: center;
  }
  .front-brand__name {
    font-weight: 700; font-size: 84px; letter-spacing: 4px;
    color: var(--card-dark-mark); line-height: 1;
  }
  .front-brand__company {
    margin-top: 10px;
    font-weight: 400; font-size: 13px; letter-spacing: 7px;
    text-transform: uppercase; color: #1f1f21;
  }
  /* Back */
  .card--back { background: var(--card-light); color: var(--ink); }
  .back-brand {
    position: absolute; right: 34px; top: 26px;
    font-weight: 700; font-size: 50px; letter-spacing: 2px;
    color: var(--ink-soft); line-height: 1;
  }
  .identity {
    position: absolute; left: 34px; top: 112px;
    padding-left: 14px;
    border-left: 6px solid var(--ink-strong);
  }
  .identity__name { font-size: 21px; font-weight: 400; color: var(--ink); line-height: 1.1; }
  .identity__name strong { font-weight: 700; color: var(--ink-strong); }
  .identity__title { font-size: 13px; color: var(--ink); margin-top: 3px; }
  .contacts {
    position: absolute; left: 34px; top: 180px;
    list-style: none;
  }
  .contacts__item {
    display: flex; align-items: center; gap: 10px;
    font-size: 13px; color: var(--ink); height: 20px;
  }
  .contacts__icon { width: 12px; height: 12px; flex: none; fill: var(--ink-soft); }
  .footer-rule {
    position: absolute; left: 34px; right: 160px; bottom: 32px;
    border-top: 2px solid var(--rule);
  }
  .website {
    position: absolute; right: 34px; bottom: 25px;
    font-size: 13px; color: var(--ink);
  }
</style>
</head>
<body>
<main class="canvas">
  <section class="card card--front" aria-label="Card front">
    <div class="front-brand">
      <div class="front-brand__name">KIRO</div>
      <div class="front-brand__company">Kiro Harbour Limited</div>
    </div>
  </section>

  <section class="card card--back" aria-label="Card back">
    <div class="back-brand">KIRO</div>
    <div class="identity">
      <p class="identity__name">Dorian <strong>Pallister</strong></p>
      <p class="identity__title">Job title</p>
    </div>
    <ul class="contacts">
      <li class="contacts__item">
        <svg class="contacts__icon" viewBox="0 0 12 12" aria-hidden="true"><rect x="2.5" y="0.5" width="7" height="11" rx="1.2" fill="none" stroke="#6d6d70" stroke-width="1.2"/><circle cx="6" cy="9.6" r="0.7"/></svg>
        (212) 555-0143
      </li>
      <li class="contacts__item">
        <svg class="contacts__icon" viewBox="0 0 12 12" aria-hidden="true"><path d="M1 3.5C1 2 2.5 1.5 6 1.5S11 2 11 3.5v1H8.5V3.2h-5v1.3H1z"/><rect x="2" y="5.5" width="8" height="5.5" rx="1"/></svg>
        1 (212) 555-0178
      </li>
      <li class="contacts__item">
        <svg class="contacts__icon" viewBox="0 0 12 12" aria-hidden="true"><rect x="0.5" y="2.5" width="11" height="7.5"/><path d="M0.8 2.8L6 7l5.2-4.2" fill="none" stroke="#fff" stroke-width="0.9"/></svg>
        dorian27@kiroharbour-mail.com
      </li>
      <li class="contacts__item">
        <svg class="contacts__icon" viewBox="0 0 12 12" aria-hidden="true"><path d="M6 0.5a4 4 0 0 1 4 4c0 3-4 7-4 7s-4-4-4-7a4 4 0 0 1 4-4z"/><circle cx="6" cy="4.5" r="1.5" fill="#fff"/></svg>
        482 Halden Ave, New York, NY 10160, USA
      </li>
    </ul>
    <div class="footer-rule"></div>
    <div class="website">kiroharbour-web.com</div>
  </section>
</main>
</body>
</html>
```